Soft furnishing company selling fabrics, curtains, bedlinen craft & haberdashery

We need 4 x home page banners for our website as follows:
Image 1 - to lead customers to our "New season Fabrics" page,
Image 2 - to lead customers to our Ready Made curtains,
Image 3 - to lead customers to our "Polar Bear Bed linen" page
Image 4 - to lead customers to our "Christmas raft Tutorial" page

Banner needs to be 960px wide x 380px 72dpi and optimised for web. should have a little descriptive text for example "Fabulous Fabric. Prints, plains & weaves, view our range of new season furnishing fabrics to buy by the metre" "Instantly update your home with our range of ready made curtains. Available . "Cosy Night In. Snuggle with this Polar Bear Duvet Set. From €20" "" "Let's Get Crafting for Christmas. Download our free Project and tutoirals here. First 3 images need a "shop now" button

website url www.lintelnest.ie

Target Market(s)

Female 25 -45

Industry/Entity Type

It Company

Font styles to use
Serif
Sans Serif

Requirements
Must have
• shop now button on image 1, 2, 3
Should not have
• too much text or clutter

```html
<!DOCTYPE html>
<html lang="en">
<head>
<meta charset="utf-8">
<title>Cosy Night In – Polar Bear Duvet Set</title>
<link rel="stylesheet" href="https://fonts.googleapis.com/css2?family=Roboto:wght@100;300;400&display=swap">
<style>
  :root {
    --panel-taupe: #5a5250;
    --text-white: #ffffff;
    --button-gold: #c3984a;
    --wall-wood: #8c7e72;
    --floor-wood: #cbbcaa;
    --bed-light: #ebe8e5;
    --bed-shade: #d6d0cb;
    --throw-grey: #7d726b;
    --rug-grey: #a29a93;
  }
  html, body {
    margin: 0;
    padding: 0;
    overflow: hidden;
  }
  .banner {
    position: relative;
    width: 1200px;
    height: 475px;
    display: flex;
    font-family: "Roboto", "Helvetica Neue", Arial, sans-serif;
    overflow: hidden;
  }
  .banner__panel {
    width: 481px;
    height: 100%;
    background: var(--panel-taupe);
    color: var(--text-white);
    display: flex;
    flex-direction: column;
    align-items: center;
    padding-top: 146px;
    box-sizing: border-box;
  }
  .banner__title {
    margin: 0;
    font-weight: 100;
    font-size: 57px;
    line-height: 1;
    letter-spacing: 0.3px;
    white-space: nowrap;
  }
  .banner__copy {
    margin: 8px 0 0;
    font-weight: 400;
    font-size: 22px;
    line-height: 1.38;
    letter-spacing: -0.2px;
    text-align: center;
  }
  .banner__button {
    margin-top: 16px;
    display: inline-block;
    background: var(--button-gold);
    color: var(--text-white);
    text-decoration: none;
    font-weight: 400;
    font-size: 22px;
    line-height: 44px;
    padding: 0 27px;
  }
  .banner__photo {
    flex: 1;
    height: 100%;
    background:
      radial-gradient(ellipse 34% 62% at 48% 64%, var(--bed-light) 0%, var(--bed-light) 55%, rgba(235,232,229,0) 100%),
      radial-gradient(ellipse 16% 22% at 58% 36%, var(--throw-grey) 0%, rgba(125,114,107,0) 100%),
      radial-gradient(ellipse 14% 40% at 97% 78%, var(--rug-grey) 0%, rgba(162,154,147,0) 100%),
      radial-gradient(ellipse 12% 18% at 90% 18%, #9c918a 0%, rgba(156,145,138,0) 100%),
      linear-gradient(180deg, var(--wall-wood) 0%, var(--bed-shade) 22%, var(--floor-wood) 60%, var(--floor-wood) 100%);
  }
</style>
</head>
<body>
  <section class="banner">
    <div class="banner__panel">
      <h1 class="banner__title">COSY NIGHT IN</h1>
      <p class="banner__copy">Snuggle with this Polar Bear<br>Duvet Set. From €20</p>
      <a class="banner__button" href="#">Shop Now</a>
    </div>
    <div class="banner__photo" role="img" aria-label="Bedroom scene with a polar bear family printed duvet set, matching pillows and cushion, a grey faux fur throw, bedside table, candles, a tufted armchair and a grey rug on a light wooden floor"></div>
  </section>
</body>
</html>
```